K7 Digital Stationery Design Project

We are looking to have stationary designs created for our company branding materials. We are looking for the following to be created.
1. Business Cards (front & back)
2. Letterhead
3. Envelopes #10
We are a new web design, development and marketing firm. Primary color scheme is desired to be blue/grey/white. This web start-up is owned and operated by individuals with 15+ years experience each in the industry so should not look as though it is a start-up by young/inexperienced individuals.
We build website & custom applications/software. In addition we provide the full spectrum of web marketing solutions including SEO, PPC, Social Media, Branding, Content Marketing and PR.
Please let us know if you have any questions. Looking forward to seeing all the amazing design ideas.
Attached is our logo.
Thanks!
Target Market(s)
Company will be nearly 100% business to business sales. Looking to work with companies that are already established, with a website, who want to take their website and/or online marketing efforts to the next level.
Industry/Entity Type
Marketing
Look and feel

```html
<!DOCTYPE html>
<html lang="en">
<head>
<meta charset="utf-8">
<title>K7 Digital – Business Cards</title>
<link rel="stylesheet" href="https://fonts.googleapis.com/css2?family=Source+Sans+3:wght@400;600;700&display=swap">
<style>
  :root {
    --page-bg: #e4e5e7;
    --card-white: #f4f4f4;
    --ink-dark: #2e2f33;
    --ink-body: #3c3d40;
    --brand-blue: #1b7fc9;
    --blue-deep: #1570c2;
    --blue-light: #0c98cf;
    --on-blue: #ffffff;
  }
  * { box-sizing: border-box; margin: 0; padding: 0; }
  html, body {
    width: 1200px; height: 985px; overflow: hidden;
    background: var(--page-bg);
    font-family: "Source Sans 3", "Myriad Pro", Arial, sans-serif;
  }
  .sheet {
    width: 1200px; height: 985px;
    display: flex; flex-direction: column; align-items: center; justify-content: center;
    gap: 60px;
  }
  .card {
    width: 700px; height: 400px;
    border-radius: 34px;
    position: relative;
    overflow: hidden;
    box-shadow: 0 2px 6px rgba(0,0,0,0.12);
  }

  /* Front */
  .card-front { background: var(--card-white); }
  .front-brand {
    position: absolute; left: 64px; top: 168px;
  }
  .brand-mark {
    display: flex; align-items: center; gap: 14px;
  }
  .brand-dot {
    width: 22px; height: 22px; border-radius: 50%;
    background: var(--brand-blue);
  }
  .brand-name {
    font-weight: 700; font-size: 44px; letter-spacing: 0.5px;
    color: var(--ink-dark); text-transform: uppercase; line-height: 1;
  }
  .brand-tagline {
    margin-top: 6px; font-size: 17px; color: var(--ink-body);
  }
  .contact {
    position: absolute; left: 430px; top: 78px;
    color: var(--ink-body);
  }
  .contact-name {
    font-weight: 700; font-size: 25px; color: var(--brand-blue); line-height: 1.1;
  }
  .contact-title { font-size: 16px; margin-top: 2px; }
  .contact-address { font-size: 15px; margin-top: 18px; line-height: 1.45; }
  .contact-lines { list-style: none; margin-top: 8px; font-size: 15px; line-height: 1.55; }
  .contact-lines li { display: flex; align-items: center; gap: 8px; }
  .contact-lines svg { width: 12px; height: 12px; flex: none; }

  /* Back */
  .card-back {
    background: linear-gradient(200deg, var(--blue-light) 0%, var(--blue-deep) 60%, #176bbd 100%);
    color: var(--on-blue);
  }
  .back-brand {
    position: absolute; left: 0; right: 0; top: 128px;
    text-align: center;
  }
  .card-back .brand-mark { justify-content: center; }
  .card-back .brand-dot { background: var(--on-blue); }
  .card-back .brand-name { color: var(--on-blue); }
  .card-back .brand-tagline { color: var(--on-blue); }
  .back-url {
    margin-top: 26px; font-size: 16px; letter-spacing: 0.3px;
  }
</style>
</head>
<body>
<main class="sheet">
  <section class="card card-front" aria-label="Business card front">
    <div class="front-brand">
      <div class="brand-mark">
        <span class="brand-dot"></span>
        <span class="brand-name">K7 Digital</span>
      </div>
      <p class="brand-tagline">Web Design, Development and Marketing</p>
    </div>
    <div class="contact">
      <p class="contact-name">Daniel Ferrante</p>
      <p class="contact-title">Director / Executive Chef</p>
      <p class="contact-address">220 Harbor Street<br>9th Floor / NY / NY / 10014</p>
      <ul class="contact-lines">
        <li>
          <svg viewBox="0 0 12 12" aria-hidden="true"><path d="M3 1 L5 3.5 L4 5 Q5 7 7 8 L8.5 7 L11 9 L9.5 11 Q5 11 2.5 8 Q0.5 5.5 1 2.5 Z" fill="var(--brand-blue)"/></svg>
          (555) 204-6180
        </li>
        <li>
          <svg viewBox="0 0 12 12" aria-hidden="true"><rect x="0.5" y="2" width="11" height="8" rx="1" fill="var(--brand-blue)"/><path d="M1 2.5 L6 6.5 L11 2.5" stroke="#fff" stroke-width="1" fill="none"/></svg>
          dan@k7digital.com
        </li>
        <li>
          <svg viewBox="0 0 12 12" aria-hidden="true"><circle cx="6" cy="6" r="5.5" fill="var(--brand-blue)"/><path d="M0.5 6 H11.5 M6 0.5 Q3 6 6 11.5 M6 0.5 Q9 6 6 11.5" stroke="#fff" stroke-width="0.8" fill="none"/></svg>
          www.k7digital.com
        </li>
      </ul>
    </div>
  </section>

  <section class="card card-back" aria-label="Business card back">
    <div class="back-brand">
      <div class="brand-mark">
        <span class="brand-dot"></span>
        <span class="brand-name">K7 Digital</span>
      </div>
      <p class="brand-tagline">Web Design, Development and Marketing</p>
      <p class="back-url">www.k7digital.com</p>
    </div>
  </section>
</main>
</body>
</html>
```